Specialised investor in e-mobility and energy wants business card design

We need a business card design that fits our existing corporate design. <The look and feel must be 'sharp'/'clean', dynamic, communicate momentum, professionalism etc (as one would imagine from a firm in the financial sector). We like the idea of a reverse-side of the card that includes the logo, and the name and contact details on the other. We expect the deliverable to be whatever format might be required to be able to get cards printed directly by a service such as tandor press. Our website is www.orm.capital

```html
<!DOCTYPE html>
<html lang="en">
<head>
<meta charset="utf-8">
<title>ORM Capital – Business Card</title>
<link href="https://fonts.googleapis.com/css2?family=Questrial&display=swap" rel="stylesheet">
<style>
  :root {
    --bg: #e4e5e7;
    --card: #ffffff;
    --green-dark: #1f4a12;
    --green-light: #7cbf3f;
    --text-grey: #4a4a4a;
    --rule: #3d7a23;
  }
  * { margin: 0; padding: 0; box-sizing: border-box; }
  html, body {
    width: 1200px; height: 800px; overflow: hidden;
    background: var(--bg);
    font-family: "Questrial", "Century Gothic", sans-serif;
  }
  .sheet {
    width: 1200px; height: 800px;
    display: flex; align-items: center; justify-content: center; gap: 40px;
  }
  .card {
    position: relative;
    width: 540px; height: 340px;
    background: var(--card);
    box-shadow: 0 2px 6px rgba(0,0,0,0.12);
    overflow: hidden;
  }
  .card__band {
    position: absolute; left: 0; bottom: 30px;
    width: 84%; height: 14px;
    background: var(--green-dark);
  }
  .card__accent {
    position: absolute; left: 86%; bottom: 14px;
    width: 9%; height: 16px;
    background: var(--green-light);
  }
  .wordmark {
    display: flex; align-items: center; gap: 12px;
    color: var(--green-dark);
    line-height: 1; white-space: nowrap;
  }
  .wordmark__square { background: var(--green-light); flex: none; }

  /* Logo side */
  .card--logo .wordmark {
    position: absolute; left: 70px; top: 122px;
    font-size: 58px;
  }
  .card--logo .wordmark__square { width: 22px; height: 22px; }

  /* Contact side */
  .card--contact .wordmark {
    position: absolute; right: 34px; top: 118px;
    font-size: 34px; gap: 8px;
  }
  .card--contact .wordmark__square { width: 14px; height: 14px; }

  .contact {
    position: absolute; left: 40px; top: 40px;
    color: var(--text-grey);
  }
  .contact__name {
    color: var(--green-dark);
    font-size: 18px; letter-spacing: 0.5px;
  }
  .contact__role { font-size: 14px; margin-bottom: 14px; }
  .contact__list { list-style: none; font-size: 14px; }
  .contact__list li {
    display: flex; align-items: center; gap: 10px; height: 24px;
  }
  .contact__list svg { width: 13px; height: 13px; flex: none; }
  .contact__rule {
    width: 280px; height: 1px; background: var(--rule); margin: 8px 0;
  }
  .contact__address {
    display: flex; align-items: center; gap: 8px; font-size: 14px; white-space: nowrap;
  }
  .contact__address svg { width: 13px; height: 15px; flex: none; }
  .contact__company { color: var(--green-light); }
</style>
</head>
<body>
<main class="sheet">
  <section class="card card--logo" aria-label="Card reverse side">
    <div class="wordmark"><span class="wordmark__square"></span><span>ORM Capital</span></div>
    <div class="card__band"></div>
    <div class="card__accent"></div>
  </section>

  <section class="card card--contact" aria-label="Card front side">
    <div class="contact">
      <p class="contact__name">PETER HALLWOOD</p>
      <p class="contact__role">Partner</p>
      <ul class="contact__list">
        <li>
          <svg viewBox="0 0 14 14" aria-hidden="true"><rect x="3.5" y="0.5" width="7" height="13" rx="1.5" fill="none" stroke="var(--green-light)" stroke-width="1.2"/><circle cx="7" cy="11" r="0.8" fill="var(--green-light)"/></svg>
          <span>+41 79 555 0142</span>
        </li>
        <li>
          <svg viewBox="0 0 14 14" aria-hidden="true"><rect x="1" y="3" width="12" height="8" rx="1" fill="var(--green-light)"/><path d="M1 3 L7 8 L13 3" fill="none" stroke="#fff" stroke-width="1"/></svg>
          <span>peter@orm.capital</span>
        </li>
        <li>
          <svg viewBox="0 0 14 14" aria-hidden="true"><circle cx="7" cy="7" r="5.8" fill="none" stroke="var(--green-light)" stroke-width="1.3"/><ellipse cx="7" cy="7" rx="2.5" ry="5.8" fill="none" stroke="var(--green-light)" stroke-width="1"/><line x1="1.2" y1="7" x2="12.8" y2="7" stroke="var(--green-light)" stroke-width="1"/></svg>
          <span>www.orm.capital</span>
        </li>
      </ul>
      <div class="contact__rule"></div>
      <p class="contact__address">
        <svg viewBox="0 0 14 16" aria-hidden="true"><path d="M7 0.8 A5 5 0 0 1 12 5.8 C12 9.5 7 15 7 15 C7 15 2 9.5 2 5.8 A5 5 0 0 1 7 0.8 Z" fill="var(--green-light)"/><circle cx="7" cy="5.8" r="1.9" fill="#fff"/></svg>
        <span><span class="contact__company">ORM Capital S.A.</span> Brenvale, Alpenland</span>
      </p>
    </div>
    <div class="wordmark"><span class="wordmark__square"></span><span>ORM Capital</span></div>
    <div class="card__band"></div>
    <div class="card__accent"></div>
  </section>
</main>
</body>
</html>
```